Dental Office Needs a Flyer Design to Attract New Patients

We need a flyer design for a dental office in Rockville, MD, US. Our office name is Brightpeak Dental Care. Our website is: brightpeakdentalcare.example and our office logo can be seen on the website. We would like stay that call and make an appointment with Dr. Le Ko. The flyer can follow the color scheme of our logo (blue and white). We current have Holiday/New Year special: Dental exam, x-ray, and cleaning for $95 (a $300 value); please include this in the flyer. Also if you can include a winter inspired picture to be part of the flyer, that would be great. We really like your Grin Tallowa flyer design and are looking for something similar. Thank you!
Target Market(s)
Apartment complex that is 5 minutes (less than 1 mile away)
Industry/Entity Type
Dental
Look and feel

```html
<!DOCTYPE html>
<html lang="en">
<head>
<meta charset="utf-8">
<title>Brightpeak Dental Care — New Patient Flyer</title>
<link rel="stylesheet" href="https://fonts.googleapis.com/css2?family=Jost:wght@400;500;600;700&family=Mulish:wght@400;600&display=swap">
<style>
  :root {
    --page-bg: #eef0f3;
    --paper: #ffffff;
    --teal: #5ecbd9;
    --navy: #2b3a8f;
    --navy-soft: #2e3f96;
    --offer-red: #ec2327;
    --ink: #1d1d1f;
    --photo-light: #ffffff;
    --photo-skin: #efcdb8;
    --photo-warm: #e2b49c;
    --photo-hair: #5a463e;
  }
  * { margin: 0; padding: 0; box-sizing: border-box; }
  html, body { width: 900px; height: 1200px; overflow: hidden; background: var(--page-bg); }
  body { position: relative; font-family: "Jost", sans-serif; color: var(--ink); }

  .flyer {
    position: absolute; left: 36px; top: 12px;
    width: 690px; height: 980px;
    background: var(--paper);
    transform: scale(1.2); transform-origin: 0 0;
    box-shadow: 0 2px 10px rgba(0,0,0,.18);
    overflow: hidden;
  }

  .hero-art { position: absolute; left: 0; top: 0; width: 690px; height: 570px; }

  .brand {
    position: absolute; left: 30px; top: 72px;
    display: flex; align-items: center; gap: 12px;
  }
  .brand-dot { width: 34px; height: 34px; border-radius: 50%; background: var(--navy); }
  .brand-name { font-weight: 600; font-size: 25px; color: var(--navy); letter-spacing: .3px; }

  .headline {
    position: absolute; left: 22px; top: 426px; width: 290px;
    text-align: center; color: var(--navy);
    font-weight: 600; font-size: 30px; line-height: 41px;
  }

  .welcome {
    position: absolute; left: 37px; top: 590px;
    font-weight: 600; font-size: 19px; color: var(--navy); white-space: nowrap;
  }
  .intro {
    position: absolute; left: 37px; top: 627px; width: 455px;
    font-family: "Mulish", sans-serif; font-size: 11.8px; line-height: 17px; color: var(--ink);
  }

  .section-label { font-size: 18px; color: var(--navy-soft); font-weight: 400; line-height: 22px; }
  .hours { position: absolute; left: 37px; top: 722px; }
  .hours-table { margin-top: 1px; border-collapse: collapse; font-family: "Mulish", sans-serif; font-size: 12px; }
  .hours-table td { padding: 0; line-height: 16.6px; }
  .hours-table td.day { width: 90px; }

  .address { position: absolute; left: 40px; top: 880px; }
  .address-lines { font-size: 14.5px; line-height: 20px; margin-top: 1px; }

  .offer {
    position: absolute; left: 303px; top: 717px; width: 332px; height: 155px;
    background: var(--teal); border-radius: 20px;
    text-align: center; padding-top: 6px;
    box-shadow: 0 6px 6px -4px rgba(0,0,0,.25);
  }
  .offer-title { color: var(--offer-red); font-weight: 600; font-size: 23px; line-height: 32px; }
  .offer-body { font-size: 23px; line-height: 33px; color: var(--ink); }
  .price { color: var(--offer-red); }

  .call { position: absolute; left: 338px; top: 888px; }
  .call-lead { font-size: 16.5px; }
  .call-phone { font-weight: 700; font-size: 24px; letter-spacing: .5px; margin-top: 2px; }
</style>
</head>
<body>
  <main class="flyer">
    <svg class="hero-art" viewBox="0 0 690 570">
      <defs>
        <radialGradient id="photoTone" cx="590" cy="300" r="330" gradientUnits="userSpaceOnUse">
          <stop offset="0" stop-color="var(--photo-skin)"/>
          <stop offset=".4" stop-color="var(--photo-warm)"/>
          <stop offset=".62" stop-color="var(--photo-hair)" stop-opacity=".55"/>
          <stop offset=".85" stop-color="var(--photo-light)"/>
        </radialGradient>
      </defs>
      <path class="photo-area" role="img" aria-label="Photo of a smiling woman with curly dark hair, hands near her face"
            fill="url(#photoTone)"
            d="M300,0 H690 V490 C640,530 570,555 500,560 L465,556 C455,500 480,440 530,400 C450,415 380,440 300,440 Z"/>
      <path class="hero-band" fill="var(--teal)"
            d="M22,292 C70,370 170,436 312,438 L312,532 Q312,555 289,555 L45,555 Q22,555 22,532 Z"/>
      <path class="swoosh-top" fill="var(--navy)"
            d="M296,436 C380,440 450,412 532,398 C470,418 400,446 300,446 Z"/>
      <path class="swoosh-bottom" fill="var(--navy)"
            d="M492,558 C570,552 640,526 690,488 L690,500 C640,542 570,564 492,564 Z"/>
    </svg>

    <div class="brand">
      <span class="brand-dot"></span>
      <span class="brand-name">Brightpeak Dental Care</span>
    </div>

    <h1 class="headline">We Love<br>To Bring Forth<br>Your Smile!</h1>

    <h2 class="welcome">Welcome to Brightpeak Dental Care in Rockville, MD</h2>
    <p class="intro">We are always welcoming new patients and we would love to have you as part of our dental family.&nbsp; Please explore our web site to learn more about us.&nbsp; You can find information about our staff, our office, and the procedures and services that we offer.</p>

    <section class="hours">
      <h3 class="section-label">Business Hours</h3>
      <table class="hours-table">
        <tr><td class="day">Monday:</td><td>9:00AM - 6:00PM</td></tr>
        <tr><td class="day">Tuesday:</td><td>Closed</td></tr>
        <tr><td class="day">Wednesday:</td><td>9:00AM - 6:00PM</td></tr>
        <tr><td class="day">Thursday:</td><td>9:00AM - 6:00PM</td></tr>
        <tr><td class="day">Friday:</td><td>9:00AM - 6:00PM</td></tr>
        <tr><td class="day">Saturday:</td><td>9:00AM - 3:00PM</td></tr>
        <tr><td class="day">Sunday:</td><td>Closed</td></tr>
      </table>
    </section>

    <section class="address">
      <h3 class="section-label">Address:</h3>
      <p class="address-lines">4170 Larkmoor Lane<br>Rockville, MD 20852</p>
    </section>

    <section class="offer">
      <p class="offer-title">Special Offer:</p>
      <p class="offer-body">Dental exam, x-ray, and<br>cleaning for<br><span class="price">$95</span> (a <span class="price">$300</span> value);</p>
    </section>

    <section class="call">
      <p class="call-lead">Call Today!</p>
      <p class="call-phone">301-555-0148</p>
    </section>
  </main>
</body>
</html>
```